In Search of a FANTASTIC BUSINESS CARD REFRESH AND REDESIGN

I would like to redesign the current business card for my company.  There is a parent company, Brookfane Care Group, with 2 operating companies - Brookfane Homecare and Brookfane Senior Living.
I will include the current business card design, along with the 3 logos I would like incorporated.  The business card can be two sided.  I'm looking for something clean, professional, and a fresh new look.

Target Market(s)
Hospitals, social workers, insurance agents, family members of seniors
Industry/Entity Type
Healthcare
Contact Information for Business Card
Name, title of person, address, phone number, web address, email address
Look and feel
Each slider illustrates characteristics of the customer's brand and the style your logo design should communicate.

```html
<!DOCTYPE html>
<html lang="en">
<head>
<meta charset="utf-8">
<title>Brookfane Care Group – Business Card</title>
<link rel="stylesheet" href="https://fonts.googleapis.com/css2?family=Montserrat:wght@400;500;600;700&family=EB+Garamond:ital@1&display=swap">
<style>
  :root {
    --backdrop: #9b9b9b;
    --card-light: #ffffff;
    --card-dark: #050505;
    --teal: #4f9a96;
    --pink: #e9559f;
    --ink: #1a1a1a;
    --white: #ffffff;
  }
  * { box-sizing: border-box; margin: 0; padding: 0; }
  html, body { width: 1093px; height: 1200px; overflow: hidden; }
  body {
    background: var(--backdrop);
    position: relative;
    font-family: "Montserrat", Arial, sans-serif;
  }
  .card {
    position: absolute;
    border-radius: 22px;
    overflow: hidden;
  }
  .card--front { left: 265px; top: 225px; width: 580px; height: 363px; background: var(--card-light); }
  .card--back  { left: 260px; top: 616px; width: 594px; height: 365px; background: var(--card-dark); }

  /* brand lockups: name in one colour and weight, plain square beside */
  .brand { position: absolute; display: flex; flex-direction: column; align-items: center; text-align: center; font-weight: 600; line-height: 1.1; }
  .brand__square { border-radius: 7px; margin-bottom: 10px; }

  .brand--senior-front { left: 40px; top: 126px; width: 200px; color: var(--teal); font-size: 22px; }
  .brand--senior-front .brand__square { width: 50px; height: 50px; background: var(--teal); margin-bottom: 14px; }

  .divider { position: absolute; left: 263px; top: 119px; width: 2px; height: 168px; background: var(--ink); }

  .contact { position: absolute; left: 279px; top: 117px; color: var(--ink); font-size: 13px; }
  .contact__name { color: var(--teal); font-weight: 700; font-size: 21px; line-height: 1.2; }
  .contact__title { font-size: 12.5px; margin-top: 3px; }
  .contact__address { margin-top: 22px; line-height: 18px; }
  .contact__list { list-style: none; margin-top: 14px; }
  .contact__item { display: flex; align-items: center; height: 21px; }
  .contact__icon { width: 12px; height: 12px; margin-right: 10px; fill: var(--ink); flex: none; }

  .brand--group { left: 150px; top: 49px; width: 294px; color: var(--white); font-size: 46px; letter-spacing: 0.5px; }
  .brand--group .brand__square { width: 84px; height: 84px; background: var(--white); border-radius: 10px; margin-bottom: 22px; }
  .brand--group .brand__sub { font-size: 26px; letter-spacing: 6px; margin-top: 4px; }

  .tagline {
    position: absolute; left: 150px; top: 270px; width: 294px;
    text-align: center; color: var(--white);
    font-family: "EB Garamond", Georgia, serif; font-style: italic;
    font-size: 18px; line-height: 18px;
  }

  .brand--homecare { left: 14px; top: 241px; width: 136px; color: var(--pink); font-size: 17px; }
  .brand--homecare .brand__square { width: 40px; height: 42px; background: var(--pink); }

  .brand--senior-back { left: 440px; top: 253px; width: 136px; color: var(--teal); font-size: 15px; }
  .brand--senior-back .brand__square { width: 32px; height: 34px; background: var(--teal); }
</style>
</head>
<body>

<section class="card card--front" aria-label="Card front">
  <div class="brand brand--senior-front">
    <span class="brand__square"></span>
    <span>Brookfane<br>Senior Living</span>
  </div>

  <span class="divider"></span>

  <div class="contact">
    <h1 class="contact__name">Dana Whitcombe</h1>
    <p class="contact__title">President, CEO</p>
    <p class="contact__address">482 Lanakila Ave, Suite 310,<br>Kailua HI 96734</p>
    <ul class="contact__list">
      <li class="contact__item">
        <svg class="contact__icon" viewBox="0 0 12 12" aria-hidden="true"><path d="M1 4c0-1.5 2.5-2.5 5-2.5S11 2.5 11 4v1H8.5V3.8h-5V5H1z M3 6h6l1.5 4.5h-9z"/></svg>
        (808) 555-0142
      </li>
      <li class="contact__item">
        <svg class="contact__icon" viewBox="0 0 12 12" aria-hidden="true"><path d="M0 2.5h12v1L6 7 0 3.5z M0 5l6 3.5L12 5v4.5H0z"/></svg>
        Dana@brookfanecare.com
      </li>
      <li class="contact__item">
        <svg class="contact__icon" viewBox="0 0 12 12" aria-hidden="true"><circle cx="6" cy="6" r="5.5"/><path d="M3 3.5l2 1-1 2 1.5 1.5-.5 2.5M8 2.5l-.5 2 2 1" stroke="#fff" stroke-width="1" fill="none"/></svg>
        www.brookfanecare.com
      </li>
    </ul>
  </div>
</section>

<section class="card card--back" aria-label="Card back">
  <div class="brand brand--group">
    <span class="brand__square"></span>
    <span>Brookfane</span>
    <span class="brand__sub">CARE GROUP</span>
  </div>

  <p class="tagline">Steady hands for every family…<br>Every single day.</p>

  <div class="brand brand--homecare">
    <span class="brand__square"></span>
    <span>Brookfane<br>Homecare</span>
  </div>

  <div class="brand brand--senior-back">
    <span class="brand__square"></span>
    <span>Brookfane<br>Senior Living</span>
  </div>
</section>

</body>
</html>
```